Pages toward Inner Calm - book cover

12/18 update: Please read the entire brief. I don’t love anything that has been provided up to today. Please use the graphics and colors I’ve attached!!!! Show me your creations.

I am looking for a book cover design. It is a mental health journal. Needs to be very warm, inviting, calming. I’m very interested in new creative ideas. It will be wire-o bound and also in hard copy front and back. Use the graphic and colors I already have attached to this file. It’s called “Pages Toward Inner Calm”. Self means soul or spirit or center. The idea of integration may be a fit here in some way. If some words need to be emphasized in the design, “Self” and “QRM” would be the most important. size 6"x9". The words on the front can be smaller and more inviting then they would normally be on a fiction paperback.

Update 12/16: I am not excited about any of the submissions so far. I’m looking forward to seeing more options.

Target Market(s)

Adults 30-60. Male and female. People who like to learn. People wanting to heal. Middle and upper income.

Industry/Entity Type

Mental health. Wellness

Font styles to use
Other font styles liked:
• Whatever font is used in my logo. i don’t know the name. I also would be open to a different font if it was warm, inviting, and calm.

Colors
0094D4
00A9DD
6FCCEA
C7EBF8
E9F6FB

Requirements
Must have
• My logo colors. The words “Pages Toward Inner Calm” and “A 13-Week QRM Exploration”
Nice to have
• I’d like to see some creative ideas. More abstract than realistic.
Should not have
• No realist art or photos.

```html
<!DOCTYPE html>
<html lang="en">
<head>
<meta charset="utf-8">
<title>Pages toward Inner Calm – Book Cover</title>
<link rel="stylesheet" href="https://fonts.googleapis.com/css2?family=Marcellus&family=Allura&family=Montserrat:wght@800&display=swap">
<style>
  :root {
    --blue-deep: #0094D4;
    --blue-mid: #00A9DD;
    --blue-light: #6FCCEA;
    --blue-pale: #C7EBF8;
    --blue-mist: #E9F6FB;
    --paper: #ececec;
    --paper-light: #f6f6f6;
    --teal-ink: #1f4a52;
    --white: #ffffff;
  }
  * { margin: 0; padding: 0; box-sizing: border-box; }
  html, body {
    width: 1200px; height: 675px; overflow: hidden;
    background: var(--white);
  }
  .stage {
    position: relative; width: 1200px; height: 675px;
  }
  .cover {
    position: absolute; left: 402px; top: 0;
    width: 422px; height: 675px; overflow: hidden;
    background: radial-gradient(ellipse at 50% 55%, var(--paper-light) 0%, var(--paper) 75%);
  }
  .title-top {
    position: absolute; left: 0; right: 0; top: 18px;
    text-align: center;
    font-family: "Marcellus", serif;
    font-size: 47px; letter-spacing: 1px; white-space: nowrap;
    background: linear-gradient(90deg, var(--blue-light), var(--blue-mid) 60%, var(--blue-light));
    -webkit-background-clip: text; background-clip: text; color: transparent;
  }
  .title-script {
    position: absolute; left: 150px; top: 58px;
    font-family: "Allura", cursive;
    font-size: 66px; line-height: 1;
    background: linear-gradient(180deg, var(--blue-mid), var(--blue-pale));
    -webkit-background-clip: text; background-clip: text; color: transparent;
  }
  .studio-mark {
    position: absolute; left: 286px; top: 112px;
    display: flex; align-items: center; gap: 6px;
    font-family: "Marcellus", serif;
    font-size: 11px; letter-spacing: 2px; line-height: 1.3;
    color: var(--teal-ink);
  }
  .studio-mark .dot {
    width: 12px; height: 12px; border-radius: 50%;
    border: 1px solid var(--teal-ink);
  }
  .floral-art {
    position: absolute; left: 95px; top: 153px;
    width: 212px; height: 398px;
    border-radius: 46% 50% 48% 44% / 30% 30% 32% 30%;
    background:
      radial-gradient(circle at 45% 20%, #f4ecdc 0 14%, transparent 28%),
      radial-gradient(circle at 40% 45%, #f2c2b4 0 16%, transparent 32%),
      radial-gradient(circle at 70% 62%, #f1b39f 0 16%, transparent 30%),
      radial-gradient(circle at 38% 78%, #efb8b0 0 14%, transparent 28%),
      radial-gradient(ellipse at 50% 50%, #9ab59a 0%, #c9d6c4 55%, rgba(236,236,236,0) 72%);
    filter: blur(2px);
  }
  .title-vertical {
    position: absolute; left: 170px; top: 194px; width: 80px;
    text-align: center;
    font-family: "Montserrat", sans-serif; font-weight: 800;
    font-size: 82px; line-height: 84px;
    color: var(--white);
  }
  .title-vertical span { display: block; }
  .subtitle {
    position: absolute; left: 0; right: 0; top: 568px;
    text-align: center; white-space: nowrap;
    font-family: "Marcellus", serif;
    font-size: 30px;
    color: var(--blue-deep);
    text-shadow: 0 2px 4px rgba(0,0,0,0.12);
  }
  .author-band {
    position: absolute; left: 0; right: 0; bottom: 0; height: 45px;
    background: linear-gradient(90deg, var(--blue-deep), var(--blue-light) 50%, var(--blue-mid));
    display: flex; align-items: center; justify-content: center;
  }
  .author-name {
    font-family: "Marcellus", serif;
    font-size: 31px; letter-spacing: 1px;
    color: var(--white);
  }
</style>
</head>
<body>
<div class="stage">
  <div class="cover">
    <h1 class="title-top">PAGES TOWARD</h1>
    <div class="title-script">Inner</div>
    <div class="studio-mark">
      <span class="dot"></span>
      <span>LINDEN<br>WELLNESS</span>
    </div>
    <div class="floral-art" role="img" aria-label="Soft vertical arrangement of blush roses, cream ranunculus and eucalyptus leaves"></div>
    <div class="title-vertical" aria-label="Calm">
      <span>C</span><span>A</span><span>L</span><span>M</span>
    </div>
    <p class="subtitle">A 13-Week QRM Exploration</p>
    <div class="author-band">
      <span class="author-name">AUTHOR NAME</span>
    </div>
  </div>
</div>
</body>
</html>
```